Meadowbrook Fellowship Chapel Banner Design

Designing 6 banners (3 + 3 that will hang on opposite sides of our auditorium) that are 10 feet long by 4 feet wide.

Use our branding guide - specifically item 4 (vertical logo) and item 5 (icon logo).

Design elements found in our AWAKE booklet, we would like to see designs that utilize the white, green and blue colour palettes but NOT the grey. Other colours may be incorporated (e.g. coral).

We are looking for 3 banner designs that would match on either side of the auditorium, the first banner incorporating the word "TRUTH", the second incorporating the word "LOVE", and the third incorporating the word "MISSION".

We interested in incorporating graphics such as trees or outdoor themes.

Font styles to use
Other font styles liked:
• Montserrat

Colors
34a7d7
00a990
f47c35

Requirements
Must have
• Banner Type #1 include the word "TRUTH"
Banner Type #2 include the word "LOVE"
Banner Type #3 include the word "MISSION"

Colour scheme must include CMYK 54 / 5 / 16 / 0 (which is available in the branding guide.) We have selected the three colours, included below in the brief.

From the branding guide - utilize #5 (icon) for the banner.

UPDATE: After reviewing the initial submissions, we are asking for designs that ONLY incorporate #5 - the ICON logo for the banners.
Nice to have
• It would be nice to have some creativity with the colour ... though a more minimalistic style is preferred.

Graphic adaptations such as trees in the background would be of interest.
Should not have
• Colour scheme should not be gray scale.

The banners should NOT be too busy.

Scripture verses (written out) are not necessary.

```html
<!DOCTYPE html>
<html lang="en">
<head>
<meta charset="utf-8">
<title>Meadowbrook Fellowship Chapel – Auditorium Banners</title>
<link rel="stylesheet" href="https://fonts.googleapis.com/css2?family=Montserrat:wght@700;900&display=swap">
<style>
  :root {
    --stage: #5c5c5c;
    --banner-white: #ffffff;
    --border-soft: #8a8a8a;
    --border-dark: #111111;
    --peach-light: #fbab80;
    --peach-mid: #f39a6a;
    --coral-deep: #e07a4a;
    --word-white: #ffffff;
    --brand-teal: #5bbccc;
  }
  * { box-sizing: border-box; margin: 0; padding: 0; }
  html, body {
    width: 1200px;
    height: 935px;
    overflow: hidden;
    background: var(--stage);
  }
  .banner-set {
    position: relative;
    width: 1200px;
    height: 935px;
  }
  .banner {
    position: absolute;
    top: 36px;
    width: 342px;
    height: 852px;
    background: var(--banner-white);
    border: 1px solid var(--border-soft);
    overflow: hidden;
  }
  .banner--truth { left: 50px; }
  .banner--love { left: 430px; }
  .banner--mission { left: 814px; border-color: var(--border-dark); }

  .banner__scene {
    position: absolute;
    left: 0;
    top: 0;
    width: 100%;
    height: 647px;
    background:
      linear-gradient(180deg, transparent 72%, rgba(224,122,74,0.45) 100%),
      linear-gradient(105deg, var(--peach-light) 0%, var(--peach-mid) 55%, var(--coral-deep) 100%);
  }
  .banner__word {
    position: absolute;
    top: 90px;
    left: 116px;
    width: 124px;
    height: 545px;
    writing-mode: vertical-rl;
    transform: rotate(180deg);
    text-align: end;
    font-family: "Montserrat", sans-serif;
    font-weight: 900;
    font-size: 128px;
    line-height: 124px;
    color: var(--word-white);
    white-space: nowrap;
  }
  .banner--mission .banner__word {
    left: 104px;
    width: 112px;
    font-size: 114px;
    line-height: 112px;
  }

  .banner__brand {
    position: absolute;
    left: 0;
    top: 647px;
    width: 100%;
    height: 205px;
    display: flex;
    align-items: center;
    justify-content: center;
    gap: 10px;
    padding: 0 24px;
  }
  .brand__dot {
    flex: none;
    width: 22px;
    height: 22px;
    border-radius: 50%;
    background: var(--brand-teal);
  }
  .brand__name {
    font-family: "Montserrat", sans-serif;
    font-weight: 700;
    font-size: 19px;
    line-height: 1.2;
    color: var(--brand-teal);
    text-align: left;
  }
</style>
</head>
<body>
  <main class="banner-set">
    <section class="banner banner--truth">
      <div class="banner__scene" role="img" aria-label="Illustration of a stylised leafy tree over rolling hills in coral and peach tones"></div>
      <h2 class="banner__word">TRUTH</h2>
      <footer class="banner__brand">
        <span class="brand__dot"></span>
        <span class="brand__name">Meadowbrook<br>Fellowship Chapel</span>
      </footer>
    </section>

    <section class="banner banner--love">
      <div class="banner__scene" role="img" aria-label="Illustration of a stylised leafy tree over rolling hills in coral and peach tones"></div>
      <h2 class="banner__word">LOVE</h2>
      <footer class="banner__brand">
        <span class="brand__dot"></span>
        <span class="brand__name">Meadowbrook<br>Fellowship Chapel</span>
      </footer>
    </section>

    <section class="banner banner--mission">
      <div class="banner__scene" role="img" aria-label="Illustration of a stylised leafy tree over rolling hills in coral and peach tones"></div>
      <h2 class="banner__word">MISSION</h2>
      <footer class="banner__brand">
        <span class="brand__dot"></span>
        <span class="brand__name">Meadowbrook<br>Fellowship Chapel</span>
      </footer>
    </section>
  </main>
</body>
</html>
```